School learning environment project dashboard

We have an online learning enviroment for schools (12 / 18 year). Within this enviroment students work on projects.

Attached we have a setup we have created for a project, but we are looking for more ideas to make this even better, more sexy and still keep it functional for teachers and students.

The attached files show one dashboard we have. This dashboard holds the roadmap for the student, upcoming appointments, latest messages and the main documents the student is working on.

Target Market(s)

schools

Number of Pages Required

1 page

Font styles to use
Sans Serif

```html
<!DOCTYPE html>
<html lang="en">
<head>
<meta charset="utf-8">
<title>Student project dashboard</title>
<link href="https://fonts.googleapis.com/css2?family=Catamaran:wght@400;500;600;700&display=swap" rel="stylesheet">
<style>
:root{
  --page:#ffffff;
  --edge:#8d7f98;
  --side:#b3a7bd;
  --main:#9d8fa3;
  --head:#3a2a42;
  --head-tint:#7a6b85;
  --ink:#2a1d33;
  --white:#ffffff;
  --muted:#d7cedc;
  --blue:#2b9ce0;
  --green:#3bc71b;
  --green-soft:#c8f0a8;
  --blue-soft:#bcdcf4;
  --yellow:#d9e021;
  --yellow-soft:#f7e4b0;
  --pink:#e2196a;
  --pink-soft:#f6c4dc;
  --track:#dcd3e0;
  --olive:#bdb86a;
  --paper:#d8d0dc;
  --bubble:#ddd0e6;
  --footer:#bde3f7;
  --panel:#bfe6fb;
}
*{box-sizing:border-box;margin:0;padding:0}
html,body{width:1200px;height:1200px;overflow:hidden;background:var(--page);font-family:"Catamaran",sans-serif;font-variant-numeric:lining-nums}
.screen{position:absolute;top:357px;width:896px;height:788px;transform:scale(.625);transform-origin:0 0;background:var(--main);overflow:hidden;box-shadow:0 6px 18px rgba(0,0,0,.18)}
.screen--view{left:32px}
.screen--compose{left:616px}
.abs{position:absolute}
.edge{left:0;top:0;width:36px;height:788px;background:var(--edge)}
.sidebar{left:36px;top:0;width:189px;height:788px;background:var(--side)}
.header-photo{left:225px;top:0;width:671px;height:90px;background:linear-gradient(100deg,#2c1f35 0%,#4b3a4f 35%,#6d5a60 60%,#3a2a3c 100%)}
.header-user{left:0;top:0;width:225px;height:90px;background:var(--head-tint)}
.avatar{left:38px;top:37px;width:52px;height:52px;border-radius:50%;background:linear-gradient(#c9a58a,#6b5a55);border:3px solid var(--green)}
.welcome{left:97px;top:45px;color:var(--green);font-size:15px;font-weight:600}
.user-name{left:97px;top:63px;color:var(--white);font-size:16px;font-weight:700}
.brand{left:251px;top:12px;color:var(--white);font-size:22px;font-weight:700}
.crumbs{left:251px;top:69px;color:var(--white);font-size:9px}
.crumbs b{color:#39b6f0;font-weight:500}
.top-icon{top:20px;width:16px;height:16px;border-radius:50%;background:var(--ink);border:1px solid #fff}
.tabs{left:251px;top:110px;display:flex;gap:27px;font-size:15px;color:var(--white)}
.tabs .on{color:var(--blue);font-weight:600;border-bottom:2px solid var(--blue);padding-bottom:2px}
.tool-icon{top:112px;width:13px;height:12px;border-radius:3px;background:var(--ink)}
.menu{left:52px;top:146px;width:160px}
.menu li{list-style:none;display:flex;align-items:center;height:42px;font-size:15px;color:var(--ink)}
.menu li i{width:12px;height:11px;border-radius:3px;background:var(--ink);margin-right:16px;display:inline-block}
.menu .strong{font-weight:700}
.menu .current span{border-bottom:2px solid var(--ink)}
.menu .gap{margin-top:28px}
.screen--compose .menu .dim{color:#d8cfdd}
.screen--compose .menu .dim i{background:#8c7f95}
.burger{left:197px;top:151px}
.title{color:var(--white);font-size:15px;font-weight:700}
.link{color:var(--white);font-size:11px}
.timeline{left:251px;top:197px;width:591px;height:71px;background:var(--track);border:2px solid var(--yellow);border-radius:6px}
.step{position:absolute;top:17px;width:34px;height:34px;border-radius:50%;font-size:14px;font-weight:700;color:var(--ink);display:flex;align-items:center;justify-content:center}
.step small{position:absolute;top:37px;font-size:8px;font-weight:400;color:#9a8fa2;white-space:nowrap}
.badge{position:absolute;top:-8px;right:-4px;width:14px;height:14px;border-radius:3px}
.dots{position:absolute;top:34px;height:0;border-top:1.5px dotted #9a8fa2}
.doc{left:251px;width:268px;height:54px;border-radius:5px;border:2px solid #e6e07a;display:flex;align-items:center;padding-left:16px;font-size:15px;color:var(--ink)}
.doc .ico{width:11px;height:11px;border-radius:3px;background:var(--ink);margin-right:10px}
.doc .acts{margin-left:auto;display:flex;gap:17px;padding-right:18px}
.doc .acts i{width:15px;height:12px;border-radius:3px;background:var(--ink);display:block}
.doc .acts i.soft{background:#8d7f98}
.doc--paper{background:var(--paper);color:#8d7f98}
.doc--plan{background:var(--olive)}
.doc--ppt{background:var(--white);border-color:#f1f0d8}
.screen--compose .doc--plan{color:#6f6a3f}
.appt{left:555px;width:268px;height:54px;border:1.5px solid var(--ink);border-radius:5px;padding:15px 17px 0;color:var(--white);font-size:13px}
.appt small{display:block;font-size:8px;color:#c8bccf;margin-top:-2px}
.appt .mark{position:absolute;right:17px;top:21px;width:10px;height:10px;border-radius:2px}
.pill{left:788px;top:379px;width:53px;height:15px;border-radius:8px;background:#dff5d0;font-size:8px;color:var(--ink);text-align:center;line-height:15px}
.poster{left:555px;top:614px;font-size:11px;font-weight:700;color:var(--ink)}
.date{left:721px;top:616px;font-size:8px;color:var(--ink)}
.bubble{left:556px;top:635px;width:231px;height:37px;background:var(--bubble);border-radius:4px;padding:7px 16px;font-size:8px;line-height:11px;color:var(--ink)}
.post-avatar{left:802px;top:638px;width:31px;height:31px;border-radius:50%;background:linear-gradient(#d8b48e,#6e5747);border:2px solid #fff}
.chat{width:18px;height:18px;border-radius:50%;background:var(--ink)}
.footer{left:225px;top:752px;width:671px;height:36px;background:var(--footer);font-size:9px;color:var(--ink);text-align:right;padding:12px 36px 0 0}
.footer b{color:var(--blue);font-weight:700}
.edge-foot{left:0;top:752px;width:36px;height:36px;background:var(--footer)}
.compose{left:629px;top:431px;width:221px;height:285px;background:var(--panel);border:2px solid #d8f0fd;border-radius:12px;box-shadow:0 4px 14px rgba(0,0,0,.15)}
.compose .env{position:absolute;left:23px;top:16px;width:35px;height:35px;background:var(--white);border-radius:6px;display:flex;align-items:center;justify-content:center}
.compose .env i{width:14px;height:11px;background:var(--ink);border-radius:2px;display:block}
.compose h2{position:absolute;left:70px;top:26px;color:#1fa4e6;font-size:11px;font-weight:700}
.compose .close{position:absolute;right:14px;top:8px;width:13px;height:13px;border-radius:3px;background:var(--pink)}
.field{position:absolute;left:23px;width:179px;height:27px;background:#d9effb;border-radius:5px;font-size:8px;color:#6d6a78;padding:8px 9px}
.send{position:absolute;left:23px;top:240px;width:179px;height:27px;background:var(--green);border-radius:5px;color:var(--white);font-size:10px;font-weight:700;text-align:center;line-height:27px}
.more{left:870px;top:583px;color:var(--white);font-size:11px}
</style>
</head>
<body>

<section class="screen screen--view">
  <div class="abs edge"></div>
  <div class="abs sidebar"></div>
  <div class="abs header-photo" role="img" aria-label="Photo of hands typing on a laptop keyboard"></div>
  <div class="abs header-user"></div>
  <div class="abs avatar" role="img" aria-label="Student profile photo"></div>
  <div class="abs welcome">Welcome</div>
  <div class="abs user-name">Jonas Verbeek</div>
  <div class="abs brand">Studyline</div>
  <div class="abs crumbs">Dashboard &rsaquo; Projects &rsaquo; Profile paper Havo 2020-2021 &rsaquo; <b>Example</b></div>
  <div class="abs top-icon" style="left:818px"></div>
  <div class="abs top-icon" style="left:844px"></div>

  <div class="abs tabs"><span class="on">Progress</span><span>Tools</span><span>Messages</span></div>
  <div class="abs tool-icon" style="left:788px"></div>
  <div class="abs tool-icon" style="left:818px"></div>
  <div class="abs tool-icon" style="left:847px"></div>

  <ul class="abs menu">
    <li class="strong"><i></i>Dashboard</li>
    <li class="current"><i></i><span>Projects</span></li>
    <li class="dim"><i></i>Online</li>
    <li class="dim"><i></i>Profile</li>
    <li class="dim"><i></i>App</li>
    <li class="dim"><i></i>Opportunities</li>
    <li class="dim"><i></i>Help</li>
    <li class="strong gap"><i></i>Tools</li>
  </ul>
  <svg class="abs burger" width="14" height="12" viewBox="0 0 14 12"><path d="M0 1h14M0 6h14M0 11h14" stroke="#2a1d33" stroke-width="1.8"/></svg>

  <div class="abs title" style="left:250px;top:164px">Timeline</div>
  <svg class="abs" style="left:790px;top:170px" width="54" height="18" viewBox="0 0 54 18"><circle cx="9" cy="9" r="7.5" fill="none" stroke="#6d5f78"/><path d="M10.5 5.5 7 9l3.5 3.5" fill="none" stroke="#6d5f78" stroke-width="1.4"/><circle cx="45" cy="9" r="8" fill="#2a1d33"/><path d="M43.5 5.5 47 9l-3.5 3.5" fill="none" stroke="#fff" stroke-width="1.6"/></svg>
  <div class="abs timeline">
    <div class="dots" style="left:56px;width:64px"></div>
    <div class="dots" style="left:160px;width:64px"></div>
    <div class="dots" style="left:264px;width:64px"></div>
    <div class="dots" style="left:368px;width:64px"></div>
    <div class="dots" style="left:472px;width:64px"></div>
    <div class="step" style="left:17px;background:var(--green-soft)">01<span class="badge" style="background:var(--green)"></span><small>00 Month</small></div>
    <div class="step" style="left:121px;background:var(--green-soft)">02<span class="badge" style="background:var(--green)"></span><small>00 Month</small></div>
    <div class="step" style="left:225px;background:var(--green-soft)">03<span class="badge" style="background:var(--green)"></span><small>00 Month</small></div>
    <div class="step" style="left:329px;background:var(--blue-soft)">04<span class="badge" style="background:var(--blue)"></span><small>00 Month</small></div>
    <div class="step" style="left:433px;background:var(--yellow-soft)">05<span class="badge" style="background:var(--yellow)"></span><small>00 Month</small></div>
    <div class="step" style="left:537px;background:var(--pink-soft)">06<span class="badge" style="background:var(--pink)"></span><small>00 Month</small></div>
  </div>

  <div class="abs title" style="left:251px;top:307px">Documents</div>
  <div class="abs doc doc--paper" style="top:340px"><span class="ico" style="background:#8d7f98"></span>Paper<span class="acts"><i class="soft"></i><i class="soft"></i><i></i></span></div>
  <div class="abs doc doc--plan" style="top:412px"><span class="ico"></span>Plan of action<span class="acts"><i></i><i class="soft"></i><i></i></span></div>
  <div class="abs doc doc--ppt" style="top:484px"><span class="ico"></span>Powerpoint<span class="acts"><i class="soft"></i><i></i></span></div>

  <div class="abs title" style="left:555px;top:307px">Upcomming appointments</div>
  <div class="abs link" style="left:812px;top:312px">View all &rsaquo;</div>
  <div class="abs appt" style="top:340px">Submittng reseach proposal<small>00 Month</small><span class="mark" style="background:var(--green)"></span></div>
  <div class="abs pill">Planning</div>
  <div class="abs appt" style="top:412px">Example<small>00 Month</small><span class="mark" style="background:var(--yellow)"></span></div>
  <div class="abs appt" style="top:484px">Evaluation<small>00 Month</small><span class="mark" style="background:var(--pink)"></span></div>

  <div class="abs title" style="left:554px;top:576px">Recent posts</div>
  <div class="abs link" style="left:812px;top:581px">View all &rsaquo;</div>
  <div class="abs poster">Sanne Bakker</div>
  <div class="abs date">4-02-2021 at 19:39</div>
  <div class="abs bubble">Lorem ipsum dolor sit amet, consectetur adipiscing elit donec consectetur semper nunc in molestie.</div>
  <div class="abs post-avatar" role="img" aria-label="Author profile photo"></div>
  <div class="abs chat" style="left:841px;top:681px"></div>

  <div class="abs edge-foot"></div>
  <div class="abs footer">Copyright 2020 <b>Studyline</b> All rights reserved</div>
</section>

<section class="screen screen--compose">
  <div class="abs edge"></div>
  <div class="abs sidebar"></div>
  <div class="abs header-photo" role="img" aria-label="Photo of hands typing on a laptop keyboard"></div>
  <div class="abs header-user"></div>
  <div class="abs avatar" role="img" aria-label="Student profile photo"></div>
  <div class="abs welcome">Welcome</div>
  <div class="abs user-name">Jonas Verbeek</div>
  <div class="abs brand">Studyline</div>
  <div class="abs crumbs">Dashboard &rsaquo; Projects &rsaquo; Profile paper Havo 2020-2021 &rsaquo; <b>Example</b></div>
  <div class="abs top-icon" style="left:818px"></div>
  <div class="abs top-icon" style="left:844px"></div>

  <div class="abs tabs"><span class="on">Progress</span><span>Tools</span><span>Messages</span></div>
  <div class="abs tool-icon" style="left:788px"></div>
  <div class="abs tool-icon" style="left:818px"></div>
  <div class="abs tool-icon" style="left:847px"></div>

  <ul class="abs menu">
    <li class="strong"><i></i>Dashboard</li>
    <li class="current"><i></i><span>Projects</span></li>
    <li class="dim"><i></i>Online</li>
    <li class="dim"><i></i>Profile</li>
    <li class="dim"><i></i>App</li>
    <li class="dim"><i></i>Opportunities</li>
    <li class="dim"><i></i>Help</li>
    <li class="strong gap"><i></i>Tools</li>
  </ul>
  <svg class="abs burger" width="14" height="12" viewBox="0 0 14 12"><path d="M0 1h14M0 6h14M0 11h14" stroke="#2a1d33" stroke-width="1.8"/></svg>

  <div class="abs title" style="left:250px;top:164px">Timeline</div>
  <svg class="abs" style="left:790px;top:170px" width="54" height="18" viewBox="0 0 54 18"><circle cx="9" cy="9" r="7.5" fill="none" stroke="#6d5f78"/><path d="M10.5 5.5 7 9l3.5 3.5" fill="none" stroke="#6d5f78" stroke-width="1.4"/><circle cx="45" cy="9" r="8" fill="#2a1d33"/><path d="M43.5 5.5 47 9l-3.5 3.5" fill="none" stroke="#fff" stroke-width="1.6"/></svg>
  <div class="abs timeline">
    <div class="dots" style="left:56px;width:64px"></div>
    <div class="dots" style="left:160px;width:64px"></div>
    <div class="dots" style="left:264px;width:64px"></div>
    <div class="dots" style="left:368px;width:64px"></div>
    <div class="dots" style="left:472px;width:64px"></div>
    <div class="step" style="left:17px;background:var(--green-soft)">01<span class="badge" style="background:var(--green)"></span><small>00 Month</small></div>
    <div class="step" style="left:121px;background:var(--green-soft)">02<span class="badge" style="background:var(--green)"></span><small>00 Month</small></div>
    <div class="step" style="left:225px;background:var(--green-soft)">03<span class="badge" style="background:var(--green)"></span><small>00 Month</small></div>
    <div class="step" style="left:329px;background:var(--blue-soft)">04<span class="badge" style="background:var(--blue)"></span><small>00 Month</small></div>
    <div class="step" style="left:433px;background:var(--yellow-soft)">05<span class="badge" style="background:var(--yellow)"></span><small>00 Month</small></div>
    <div class="step" style="left:537px;background:var(--pink-soft)">06<span class="badge" style="background:var(--pink)"></span><small>00 Month</small></div>
  </div>

  <div class="abs title" style="left:251px;top:307px">Documents</div>
  <div class="abs doc doc--paper" style="top:340px"><span class="ico" style="background:#8d7f98"></span>Paper<span class="acts"><i class="soft"></i><i class="soft"></i><i></i></span></div>
  <div class="abs doc doc--plan" style="top:412px"><span class="ico"></span>Plan of action<span class="acts"><i></i><i class="soft"></i><i></i></span></div>
  <div class="abs doc doc--ppt" style="top:484px"><span class="ico"></span>Powerpoint<span class="acts"><i class="soft"></i><i></i></span></div>

  <div class="abs title" style="left:555px;top:307px">Upcomming appointments</div>
  <div class="abs link" style="left:812px;top:312px">View all &rsaquo;</div>
  <div class="abs appt" style="top:340px">Submittng reseach proposal<small>00 Month</small><span class="mark" style="background:var(--green)"></span></div>
  <div class="abs pill">Planning</div>
  <div class="abs appt" style="top:412px">Example<small>00 Month</small><span class="mark" style="background:var(--yellow)"></span></div>
  <div class="abs appt" style="top:484px">Evaluation<small>00 Month</small><span class="mark" style="background:var(--pink)"></span></div>

  <div class="abs title" style="left:554px;top:576px">Recent posts</div>
  <div class="abs more">&rsaquo;</div>
  <div class="abs poster">Sanne Bakker</div>
  <div class="abs bubble">Lorem ipsum dolor sit amet, consectetur adipiscing elit donec consectetur semper nunc in molestie.</div>

  <div class="abs compose">
    <div class="env"><i></i></div>
    <h2>Leave a message</h2>
    <span class="close"></span>
    <div class="field" style="top:77px">Your name (Required)</div>
    <div class="field" style="top:113px">Your email (Required)</div>
    <div class="field" style="top:152px;height:71px">Your message</div>
    <div class="send">Send &#10148;</div>
  </div>
  <div class="abs chat" style="left:859px;top:699px"></div>

  <div class="abs edge-foot"></div>
  <div class="abs footer">Copyright 2020 <b>Studyline</b> All rights reserved</div>
</section>

</body>
</html>
```